Hello,
We’re looking for a new WordPress website for Follow The Tide, our company offering unique well-being retreats and workshops.
We currently have a website online (you can consult it : www.followthetide.ch), but we now need to build a new site on WordPress — more flexible, more intuitive to manage, and better aligned with our evolving needs.

What we’re looking for:
A new userfriendly WordPress site, with:
Inspiring, elegant, and modern design
Smooth user experience on desktop and mobile
Innovative design proposals – we want to be inspired !
SEO best practices
Respect of our existing color palette
The final website will need to be set up on our existing hosting provider (details can be shared later)

Pages to Include:
- Home
- Our Story
- Our Stays - with links to 5 individual pages, each describing one of our stays in detail.
- Activities – with potential links to individual descriptive pages
- Agenda
- Our Charter
- The Team
- Contact
- Blog

Required Features:
- Space for photos and videos
- Sections for testimonials and press articles
- Blog/article layout with strong readability
- Easy-to-update backend for future content
- Newsletter sign-up (pop-up and in footer)
- Additional pop-up on/off
- “Request info” buttons
- “Booking request” buttons
- Integration of our 4 pillars - Breathe · Feel · Connect · Experience - in the design (They’re currently in the footer, but we’re open to creative suggestions)

Who we are :
Follow The Tide offers well-being and personal growth stays but with a very different spirit.
We’re not a classic wellness brand. Our approach is professional, joyful, and grounded.
We create spaces where people can take a real break — breathe, slow down, and reconnect with themselves.
During our stays, people are welcomed like friends:
with warmth, respect, and no pressure.
Each program combines practices like breathwork, movement, creativity, coaching, and massages in a relaxed, beautiful setting of the French Alps.
What makes us different:
A friendly and down-to-earth atmosphere
A wide mix of activities.
A mix of inner work and simple pleasures
Private rooms, nourishing food, and shared moments
Time to talk, to laugh, to walk, or just be silent together - and feel free to be yourself
Our guests come to pause.
They leave feeling lighter, aligned, and full of life

```html
<!DOCTYPE html>
<html lang="en">
<head>
<meta charset="utf-8">
<title>Follow The Tide – Well-being Stays</title>
<link rel="stylesheet" href="https://fonts.googleapis.com/css2?family=Montserrat:wght@400;500;600;700&family=Saira+Extra+Condensed:wght@700&display=swap">
<style>
  :root {
    --blue: #163a8f;
    --teal: #69c3c0;
    --mist: #f3f9f9;
    --ink: #1d2340;
    --white: #ffffff;
  }
  * { box-sizing: border-box; margin: 0; padding: 0; }
  html, body { width: 739px; height: 1200px; overflow: hidden; background: var(--white); }
  body { font-family: "Montserrat", sans-serif; color: var(--ink); position: relative; }

  .site-header { height: 47px; display: flex; align-items: center; justify-content: space-between; padding: 0 87px; }
  .brand { font-size: 19px; font-weight: 700; color: var(--blue); letter-spacing: 0.5px; }
  .call { display: flex; align-items: center; gap: 7px; }
  .call-icon { width: 22px; height: 22px; border-radius: 50%; background: var(--blue); display: flex; align-items: center; justify-content: center; }
  .call-label { font-size: 7px; color: var(--blue); line-height: 1.1; }
  .call-number { font-size: 9px; font-weight: 600; color: var(--blue); letter-spacing: 0.3px; }

  .main-nav { height: 29px; background: var(--teal); display: flex; align-items: center; padding: 0 87px 0 88px; }
  .main-nav ul { list-style: none; display: flex; gap: 20px; flex: 1; }
  .main-nav a { font-size: 7.3px; color: var(--white); text-decoration: none; font-weight: 500; }
  .main-nav a.current { color: var(--blue); font-weight: 700; font-size: 8px; }

  .btn { display: inline-flex; align-items: center; justify-content: center; border-radius: 12px; font-size: 8px; font-weight: 600; color: var(--white); text-decoration: none; height: 22px; padding: 0 9px; }
  .btn-blue { background: var(--blue); }
  .btn-teal { background: var(--teal); }

  .hero { position: absolute; top: 76px; left: 0; width: 739px; height: 394px; overflow: hidden; }
  .hero-photo { position: absolute; inset: 0; background:
      radial-gradient(circle at 10% 28%, rgba(240,170,70,0.85), transparent 22%),
      linear-gradient(180deg, #5f7f70 0%, #3f5c4f 35%, #7f8c85 62%, #aab3b0 78%, #6d7276 100%); }
  .hero-copy { position: absolute; top: 100px; width: 100%; text-align: center; color: var(--white); }
  .hero-title { font-family: "Saira Extra Condensed", sans-serif; font-size: 48px; line-height: 1; margin-left: 10px; }
  .hero-sub { font-size: 16px; margin-top: 10px; }
  .hero-copy .btn { margin-top: 15px; height: 22px; font-size: 10px; padding: 0 9px; }
  .hero-wave { position: absolute; left: 0; bottom: 0; }

  .pillars { position: absolute; top: 500px; left: 87px; width: 565px; }
  .section-head { display: flex; justify-content: space-between; align-items: center; }
  .section-title { font-size: 25px; font-weight: 600; color: var(--blue); line-height: 1.05; }
  .section-title span { color: var(--teal); }
  .pillar-grid { display: grid; grid-template-columns: repeat(4, 137px); gap: 6px; margin-top: 24px; }
  .pillar { height: 127px; border: 1px solid #8fd0cd; border-radius: 2px; text-align: center; padding-top: 19px; box-shadow: 0 1px 3px rgba(0,0,0,0.08); }
  .pillar-icon { width: 46px; height: 40px; margin: 0 auto; border-radius: 8px; background: linear-gradient(135deg, #dbeef0, #c8e7e6); }
  .pillar h3 { font-size: 10.5px; font-weight: 600; color: var(--blue); margin-top: 12px; }
  .pillar p { font-size: 7px; line-height: 1.8; margin-top: 6px; padding: 0 8px; }

  .about { position: absolute; top: 745px; left: 0; width: 739px; height: 282px; background: var(--mist); }
  .about-inner { position: absolute; top: 39px; left: 87px; width: 565px; border-left: 1.5px solid var(--blue); padding-left: 15px; height: 164px; }
  .about .section-title { font-size: 26px; line-height: 1.2; }
  .about p { font-size: 7.8px; line-height: 1.8; margin-top: 5px; }
  .about p:first-of-type { margin-top: 14px; }
  .about .btn { position: absolute; left: 102px; top: 217px; }
  .about-deco { position: absolute; top: 40px; left: 585px; width: 60px; height: 75px; border-radius: 50% 50% 40% 40%; background: radial-gradient(circle at 40% 35%, rgba(105,195,192,0.35), rgba(105,195,192,0.05) 70%); }

  .stays { position: absolute; top: 1050px; width: 739px; text-align: center; }
  .stays .section-title { font-size: 26px; }
</style>
</head>
<body>
  <header class="site-header">
    <div class="brand">Follow The Tide</div>
    <div class="call">
      <div class="call-icon">
        <svg width="11" height="11" viewBox="0 0 24 24" fill="none" stroke="#fff" stroke-width="2"><path d="M5 3h4l2 5-2.5 1.5a11 11 0 0 0 6 6L16 13l5 2v4a2 2 0 0 1-2 2A17 17 0 0 1 3 5a2 2 0 0 1 2-2z"/></svg>
      </div>
      <div>
        <div class="call-label">Call Us</div>
        <div class="call-number">555.014.0192</div>
      </div>
    </div>
  </header>

  <nav class="main-nav">
    <ul>
      <li><a class="current" href="#">Home</a></li>
      <li><a href="#">Our Story</a></li>
      <li><a href="#">Our Stays</a></li>
      <li><a href="#">Activities</a></li>
      <li><a href="#">Agenda</a></li>
      <li><a href="#">Our Charter</a></li>
      <li><a href="#">he Team</a></li>
      <li><a href="#">Contact</a></li>
      <li><a href="#">Blog</a></li>
    </ul>
    <a class="btn btn-blue" href="#">Booking Request</a>
  </nav>

  <section class="hero">
    <div class="hero-photo" role="img" aria-label="Woman meditating on a wooden dock beside a misty forest lake at sunrise"></div>
    <div class="hero-copy">
      <h1 class="hero-title">Exhale Stress. Inhale Presence.</h1>
      <p class="hero-sub">Highlights Both Release And Mindful Engagement.</p>
      <a class="btn btn-teal" href="#">Contact Us</a>
    </div>
    <svg class="hero-wave" width="739" height="80" viewBox="0 0 739 80">
      <path d="M0 6 Q390 150 739 0 L739 80 L0 80 Z" fill="#fff"/>
      <path d="M0 3 Q180 60 430 66 Q620 66 739 0 L739 28 Q560 90 360 68 Q160 50 0 3 Z" fill="#163a8f"/>
      <path d="M0 3 Q170 55 430 56 Q620 50 700 18 Q560 65 380 62 Q170 56 0 3 Z" fill="#69c3c0"/>
    </svg>
  </section>

  <section class="pillars">
    <div class="section-head">
      <h2 class="section-title">OUR 4 <span>PILLARS</span></h2>
      <a class="btn btn-blue" href="#">Booking Request</a>
    </div>
    <div class="pillar-grid">
      <article class="pillar">
        <div class="pillar-icon" role="img" aria-label="Breathing head icon"></div>
        <h3>BREATHE</h3>
        <p>Take a deep breath and indulge in the luxury of slowing down</p>
      </article>
      <article class="pillar">
        <div class="pillar-icon" role="img" aria-label="Open hands icon"></div>
        <h3>FEEL</h3>
        <p>Feel every sensation, every emotion and holistic approach</p>
      </article>
      <article class="pillar">
        <div class="pillar-icon" role="img" aria-label="Heart in hand icon"></div>
        <h3>CONNECT</h3>
        <p>Connect fully, in a small group, in a warm, compassionate...</p>
      </article>
      <article class="pillar">
        <div class="pillar-icon" role="img" aria-label="Stars over hand icon"></div>
        <h3>EXPERIENCE</h3>
        <p>Experience the profound change and richness of each..</p>
      </article>
    </div>
  </section>

  <section class="about">
    <div class="about-deco" role="img" aria-label="Soft dandelion decoration"></div>
    <div class="about-inner">
      <h2 class="section-title">ABOUT<br>FOLLOW THE <span>TIDE</span></h2>
      <p>Follow The Tide offers well-being and personal growth stays but with a very different spirit. We’re not a classic wellness brand. Our approach is professional, joyful, and grounded. Because every moment is precious, because reconnecting with joy and with yourself is essential.</p>
      <p>Imagine a space designed to allow for a true break, where every breath counts. Through its retreats, Follow The Tide invites you on an inner and outer journey, a unique experience where each step reconnects you with your vitality and well-being.</p>
      <p>Follow The Tide is choosing a different kind of support: a cocoon of kindness, a range of practices and expertise, and a setting designed to nourish the soul, body and spirit.</p>
    </div>
    <a class="btn btn-teal" href="#">Booking Request</a>
  </section>

  <section class="stays">
    <h2 class="section-title">OUR <span>STAYS</span></h2>
  </section>
</body>
</html>
```